VELAROOT needs a label design for their product line of therapeutic CBD HEMP oil.

We are a company based out of Hawaii, USA called "VelaRoot". We are needing a new look for our labels on our 2 oz bottles of CBD hemp oil. We are using organic CBD rich hemp oil and combining it with other organic oils to help heal inflammation, skin problems, and other ailments.

We have 6 different products of CBD oils :
x 2 CBD oil tinctures ( internal) : PRIME CBD and bOTANIC BLEND
x 3 CBD DERM GUARD oils (external): CBD FACE REVIVE, CBD TORSO
OIL, and CBD DERM GUARD
x 1 CBD Therapeutic oil ( external) SOOTHERIX - Inflammation
Each product is in a 2 oz amber bottle with a black mist sprayer cap or black dropper and is a different color label. A green bottle ( prime cbd), blue (botanic), yellow(body oil), red/pink (restorative), purple( sootherix) the other colors???
I would like to use the color gold in our labels.

There is the logo for the name 'VelaRoot", an oil droplet, and hemp leaf on each bottle.
I have the descriptive text/layout for the wording to be placed on the side of the bottles which just need a little font finessing.
I have designed the labels but just cannot seem to make them look professional and would like to re create the look.

I am seeking a label that looks professional for a successful business of high quality oils.

Target Market(s)

health food stores, alternative medicines, internet,

Industry/Entity Type

Graphic Design

Requirements
Must have
• I would like the word or logo for organic on the bottle.
• There must be a small space left for the bar code.
• I would like them all to look similar just with different colors and a slight different layout to distinguish the 2 internal CBD tiinctures ( CBD PIRME, bOTANIC BLEND) + sootherix from the 3 skin care external skin oils.
Nice to have
• I would like my product to have a hemp leaf somewhere on it but not too obvious.
• I am more concerned with the front design of the bottles than the written words on the sides of the bottle. That could be worked on later.
Should not have
• my label should not look too busy!

```html
<!DOCTYPE html>
<html lang="en">
<head>
<meta charset="utf-8">
<title>VelaRoot – bOTANIC BLEND Label Set</title>
<link href="https://fonts.googleapis.com/css2?family=Marcellus&family=Quicksand:wght@400;500&display=swap" rel="stylesheet">
<style>
  :root {
    --canvas: #eef0f2;
    --label-white: #ffffff;
    --label-cream: #f6f1de;
    --ink: #2b2b2b;
    --brand-ink: #3a3a3a;
    --gold: #c9a23a;
    --gold-light: #e8cf7a;
    --lotus: #c46bb6;
    --band-blue: #3b9ad6;
    --band-purple: #8e2fa8;
    --band-gold: #cfae3c;
    --band-text: #ffffff;
  }
  * { box-sizing: border-box; margin: 0; padding: 0; }
  html, body {
    width: 1200px; height: 900px; overflow: hidden;
    background: var(--canvas);
  }
  .label-set {
    position: absolute; inset: 0;
    display: flex; justify-content: center; align-items: center; gap: 60px;
  }
  .label {
    position: relative;
    width: 300px; height: 355px;
    background: var(--label-white);
    display: flex; flex-direction: column;
    box-shadow: 0 2px 10px rgba(0,0,0,0.08);
  }
  .label--cream { background: var(--label-cream); }
  .label__top {
    flex: 1;
    position: relative;
    display: flex; flex-direction: column; align-items: center;
    padding-top: 42px;
  }
  .brand {
    display: flex; align-items: center; gap: 8px;
    font-family: "Quicksand", sans-serif;
    font-weight: 500; font-size: 26px;
    color: var(--brand-ink);
  }
  .brand__dot {
    width: 10px; height: 10px; border-radius: 50%;
    background: var(--gold);
  }
  .product-name {
    margin-top: 26px;
    font-family: "Marcellus", serif;
    font-weight: 400;
    font-size: 36px; line-height: 1.02;
    text-align: center;
    color: var(--ink);
    letter-spacing: 0.5px;
  }
  .lotus {
    position: absolute; right: 22px; bottom: 12px;
    width: 62px; height: 34px;
    background: radial-gradient(ellipse at 50% 100%, var(--lotus) 0%, rgba(196,107,182,0.75) 55%, rgba(196,107,182,0) 72%);
  }
  .gold-rule {
    height: 4px;
    background: linear-gradient(90deg, var(--gold), var(--gold-light), var(--gold));
  }
  .band {
    height: 116px;
    display: flex; flex-direction: column; align-items: center;
    padding-top: 18px;
    font-family: "Quicksand", sans-serif;
    color: var(--band-text);
    text-align: center;
  }
  .band--blue { background: var(--band-blue); }
  .band--purple { background: var(--band-purple); }
  .band--gold { background: var(--band-gold); }
  .band__dose { font-size: 15px; line-height: 1.3; font-weight: 500; }
  .band__divider {
    width: 88%; height: 1px; margin: 12px 0 10px;
    background: rgba(255,255,255,0.7);
  }
  .band__meta { font-size: 14px; font-weight: 500; }
</style>
</head>
<body>
<main class="label-set">
  <section class="label">
    <div class="label__top">
      <div class="brand"><span class="brand__dot"></span>VelaRoot</div>
      <h1 class="product-name">bOTANIC<br>BLEND</h1>
      <div class="lotus" role="img" aria-label="Pink lotus flower ornament"></div>
    </div>
    <div class="gold-rule"></div>
    <div class="band band--blue">
      <p class="band__dose">500mg Cannabidiol<br>150mg B-Caryophyllene</p>
      <div class="band__divider"></div>
      <p class="band__meta">Dietary Supplement | 1Fl Oz./30ml</p>
    </div>
  </section>

  <section class="label">
    <div class="label__top">
      <div class="brand"><span class="brand__dot"></span>VelaRoot</div>
      <h1 class="product-name">bOTANIC<br>BLEND</h1>
      <div class="lotus" role="img" aria-label="Pink lotus flower ornament"></div>
    </div>
    <div class="gold-rule"></div>
    <div class="band band--purple">
      <p class="band__dose">500mg Cannabidiol<br>150mg B-Caryophyllene</p>
      <div class="band__divider"></div>
      <p class="band__meta">Dietary Supplement | 1Fl Oz./30ml</p>
    </div>
  </section>

  <section class="label label--cream">
    <div class="label__top">
      <div class="brand"><span class="brand__dot"></span>VelaRoot</div>
      <h1 class="product-name">bOTANIC<br>BLEND</h1>
      <div class="lotus" role="img" aria-label="Pink lotus flower ornament"></div>
    </div>
    <div class="gold-rule"></div>
    <div class="band band--gold">
      <p class="band__dose">500mg Cannabidiol<br>150mg B-Caryophyllene</p>
      <div class="band__divider"></div>
      <p class="band__meta">Dietary Supplement | 1Fl Oz./30ml</p>
    </div>
  </section>
</main>
</body>
</html>
```